Falcon guarding business card

Looking for a business card for my security company

Target Market(s)

Security

Industry/Entity Type

Security

Contact Information for Business Card

Name - Dale Hutchins. Title - General manager - direct 318 642.9053 website www. falconguardingservices.example email - dale@ falconguardingservices.example

Requirements
Must have
• Logo attached

```html
<!DOCTYPE html>
<html lang="en">
<head>
<meta charset="utf-8">
<title>Falcon Guarding – Business Card</title>
<link rel="stylesheet" href="https://fonts.googleapis.com/css2?family=Michroma&family=Barlow+Semi+Condensed:wght@400;600&display=swap">
<style>
  :root {
    --backdrop: #2b2b2b;
    --card: #050505;
    --ink: #ffffff;
    --gold: #c9a24a;
    --gold-light: #f1e2b0;
    --gold-dark: #a7782c;
    --divider: #d9d9d9;
    --figure: #151515;
  }
  * { margin: 0; padding: 0; box-sizing: border-box; }
  html, body {
    width: 1200px;
    height: 732px;
    overflow: hidden;
    background: var(--backdrop);
  }
  .canvas {
    position: relative;
    width: 1200px;
    height: 732px;
  }
  .card {
    position: absolute;
    top: 242px;
    width: 436px;
    height: 248px;
    background: var(--card);
    overflow: hidden;
    box-shadow: 0 12px 24px rgba(0,0,0,0.55);
  }
  .card--front { left: 144px; }
  .card--back { left: 621px; }

  .gold-rule {
    position: absolute;
    left: 0; right: 0; bottom: 0;
    height: 5px;
    background: linear-gradient(90deg, var(--gold-dark) 0%, var(--gold-light) 22%, var(--gold-dark) 45%, var(--gold) 60%, var(--gold-light) 82%, var(--gold-dark) 100%);
  }

  .identity {
    position: absolute;
    right: 234px;
    top: 108px;
    width: 190px;
    text-align: right;
  }
  .identity__name {
    font-family: "Michroma", sans-serif;
    font-size: 13px;
    letter-spacing: 0;
    color: var(--ink);
    line-height: 1;
    white-space: nowrap;
  }
  .identity__title {
    margin-top: 5px;
    font-family: "Barlow Semi Condensed", sans-serif;
    font-size: 12px;
    color: var(--ink);
    line-height: 1;
  }

  .divider {
    position: absolute;
    left: 214px;
    top: 104px;
    width: 1px;
    height: 41px;
    background: var(--divider);
  }

  .contacts {
    position: absolute;
    left: 225px;
    top: 102px;
    list-style: none;
  }
  .contacts__item {
    display: flex;
    align-items: center;
    height: 15px;
    font-family: "Barlow Semi Condensed", sans-serif;
    font-size: 11px;
    color: var(--ink);
    white-space: nowrap;
  }
  .contacts__icon {
    width: 9px;
    height: 9px;
    margin-right: 7px;
    flex: none;
  }

  .hero-figure {
    position: absolute;
    left: 0;
    top: 4px;
    width: 436px;
    height: 240px;
    background: radial-gradient(ellipse 60% 45% at 55% 45%, var(--figure) 0%, rgba(21,21,21,0.6) 55%, rgba(5,5,5,0) 100%);
  }

  .brand {
    position: absolute;
    left: 0; right: 0;
    top: 156px;
    display: flex;
    justify-content: center;
    align-items: center;
    gap: 7px;
  }
  .brand__dot {
    width: 10px;
    height: 10px;
    border-radius: 50%;
    background: var(--gold);
  }
  .brand__name {
    font-family: "Barlow Semi Condensed", sans-serif;
    font-weight: 600;
    font-size: 24px;
    letter-spacing: 1px;
    color: var(--gold);
    line-height: 1;
  }
</style>
</head>
<body>
<main class="canvas">
  <section class="card card--front" aria-label="Business card front">
    <div class="identity">
      <p class="identity__name">DALE HUTCHINS</p>
      <p class="identity__title">General manager</p>
    </div>
    <div class="divider"></div>
    <ul class="contacts">
      <li class="contacts__item">
        <svg class="contacts__icon" viewBox="0 0 10 10" aria-hidden="true"><path d="M2.2 0.8 L3.6 2.8 L2.8 3.8 Q3.8 5.8 6.2 7.2 L7.2 6.4 L9.2 7.8 L8.4 9.2 Q4.6 9.4 0.8 4.8 Q0.6 2.2 2.2 0.8 Z" fill="var(--gold)"/></svg>
        318 642.9053
      </li>
      <li class="contacts__item">
        <svg class="contacts__icon" viewBox="0 0 10 10" aria-hidden="true"><rect x="0.5" y="2" width="9" height="6.5" fill="var(--gold)"/><path d="M0.8 2.3 L5 5.6 L9.2 2.3" fill="none" stroke="var(--card)" stroke-width="0.9"/></svg>
        dale@ falconguardingservices.example
      </li>
      <li class="contacts__item">
        <svg class="contacts__icon" viewBox="0 0 10 10" aria-hidden="true"><g fill="none" stroke="var(--gold)" stroke-width="0.9"><circle cx="5" cy="5" r="4.3"/><ellipse cx="5" cy="5" rx="1.9" ry="4.3"/><line x1="0.7" y1="5" x2="9.3" y2="5"/><line x1="1.4" y1="2.8" x2="8.6" y2="2.8"/><line x1="1.4" y1="7.2" x2="8.6" y2="7.2"/></g></svg>
        www. falconguardingservices.example
      </li>
    </ul>
    <div class="gold-rule"></div>
  </section>

  <section class="card card--back" aria-label="Business card back">
    <div class="hero-figure" role="img" aria-label="Large dark silhouette of a leaping big cat spanning the card"></div>
    <div class="brand">
      <span class="brand__dot"></span>
      <span class="brand__name">FALCON GUARDING</span>
    </div>
  </section>
</main>
</body>
</html>
```